Rocket business card

Modern business card design, use of color is good with clean space too.

Things to include on card:

Quote: I add fuel to your optometry practice

- Eyewear Sales
- Admin Duties
- Revenue Collection
- Leadership
- Tech Adoption
- COGS Reduction
- Product Sourcing
-Medical Growth

Dalton Vessey, CEO
Glint Harbor
Text Me! 847-302-1964
dalton@glintharbor.example

```html
<!DOCTYPE html>
<html lang="en">
<head>
<meta charset="utf-8">
<title>Glint Harbor Business Card</title>
<link href="https://fonts.googleapis.com/css2?family=Raleway:wght@400;500;700&display=swap" rel="stylesheet">
<style>
  :root {
    --page: #ffffff;
    --card-red: #dc372d;
    --card-white: #ffffff;
    --ink: #111111;
    --accent: #e0432a;
    --accent-warm: #ef7a25;
    --accent-gold: #f6a11f;
    --faint: #fdf0e4;
    --shadow: rgba(0,0,0,0.28);
  }
  * { margin: 0; padding: 0; box-sizing: border-box; }
  html, body { width: 1200px; height: 1200px; overflow: hidden; background: var(--page); }
  body { position: relative; font-family: "Raleway", sans-serif; color: var(--ink); }

  .card { position: absolute; left: 181px; width: 840px; box-shadow: 0 3px 8px var(--shadow); overflow: hidden; }
  .card-front { top: 78px; height: 480px; background: var(--card-red); }
  .card-back { top: 622px; height: 478px; background: var(--card-white); }

  .brand-dot { position: absolute; }
  .brand-name { position: absolute; left: 0; right: 0; text-align: center; font-weight: 700; letter-spacing: 2px; color: var(--ink); text-transform: uppercase; }
  .card-front .brand-dot { left: 326px; top: 56px; }
  .card-front .brand-name { top: 282px; font-size: 60px; }
  .tagline { position: absolute; left: 0; right: 0; top: 373px; text-align: center; font-size: 27px; font-weight: 400; color: var(--ink); text-transform: uppercase; }

  .card-back .brand-dot { left: 181px; top: 32px; }
  .card-back .brand-mark { position: absolute; left: 40px; width: 400px; top: 0; height: 240px; }
  .card-back .brand-name { top: 182px; font-size: 40px; }

  .watermark { position: absolute; left: 553px; top: 143px; }
  .contact { position: absolute; left: 509px; top: 40px; text-transform: uppercase; }
  .person-name { font-size: 32px; font-weight: 400; color: var(--accent); line-height: 1.1; }
  .person-role { font-size: 17px; margin-top: 6px; padding-bottom: 4px; display: inline-block; border-bottom: 3px solid var(--accent); }
  .details { margin-top: 38px; font-size: 21px; line-height: 1.42; }

  .divider { position: absolute; left: 29px; right: 32px; top: 316px; border-top: 2px solid var(--accent); }
  .services { position: absolute; top: 334px; list-style: none; text-transform: uppercase; font-size: 22px; line-height: 30px; }
  .services-left { left: 44px; }
  .services-right { left: 509px; }
  .services li { display: flex; align-items: center; gap: 10px; }
  .services li::before { content: ""; width: 20px; height: 20px; border-radius: 50%; background: linear-gradient(90deg, var(--accent), var(--accent-gold)); flex: none; }
</style>
</head>
<body>
  <section class="card card-front">
    <svg class="brand-dot" width="190" height="190" viewBox="0 0 190 190" aria-hidden="true">
      <defs>
        <linearGradient id="dotFront" x1="0" x2="1"><stop offset="0" stop-color="#e0432a"/><stop offset="1" stop-color="#f6a11f"/></linearGradient>
      </defs>
      <circle cx="95" cy="95" r="92" fill="url(#dotFront)"/>
    </svg>
    <div class="brand-name">Glint Harbor</div>
    <p class="tagline">I add fuel to your optometry practice</p>
  </section>

  <section class="card card-back">
    <svg class="watermark" width="270" height="270" viewBox="0 0 270 270" aria-hidden="true">
      <circle cx="135" cy="135" r="133" fill="var(--faint)"/>
    </svg>
    <div class="brand-mark">
      <svg class="brand-dot" width="124" height="124" viewBox="0 0 124 124" aria-hidden="true">
        <defs>
          <linearGradient id="dotBack" x1="0" x2="1"><stop offset="0" stop-color="#e0432a"/><stop offset="1" stop-color="#f6a11f"/></linearGradient>
        </defs>
        <circle cx="62" cy="62" r="60" fill="url(#dotBack)"/>
      </svg>
      <div class="brand-name">Glint Harbor</div>
    </div>

    <div class="contact">
      <div class="person-name">Dalton Vessey</div>
      <div class="person-role">CEO</div>
      <div class="details">
        <div>Glint Harbor</div>
        <div>Text Me! 847-302-1964</div>
        <div style="font-size:19px">dalton@glintharbor.example</div>
      </div>
    </div>

    <div class="divider"></div>
    <ul class="services services-left">
      <li>Eyewear Sales</li>
      <li>Admin Duties</li>
      <li>Revenue Collection</li>
      <li>Leadership</li>
    </ul>
    <ul class="services services-right">
      <li>Tech Adoption</li>
      <li>COGS Reduction</li>
      <li>Product Sourcing</li>
      <li>Medical Growth</li>
    </ul>
  </section>
</body>
</html>
```